Package Card - Horse Products

I require a card design for the top of a package (see photo). This product is a number holder that gets pinned on to a horse bridle or saddle blanket for competitions. It is a high quality, genuine leather, and premium product.Card is 15cm across and 6cm high. Requirements:Must have - Logo, -"Equestrian Number Holder"- Place on back for barcodeAnything else is up to you! Suggestions and ideas welcome. Card back colour can be any colour.My outcome is for it to look like a premium product

Target Market(s)

High end equestrian competitors

Colors
fbf289

Requirements
Must have
• Logo
• "Equestrian Number Holder"
• "Genuine Leather"
• Room on the back for a barcode sticker
Nice to have
• Should look up market and elegant

```html
<!DOCTYPE html>
<html lang="en">
<head>
<meta charset="utf-8">
<title>Tidewater Equestrian – Number Holder Header Card</title>
<link rel="stylesheet" href="https://fonts.googleapis.com/css2?family=Marcellus&family=Oswald:wght@600&family=Open+Sans:wght@700&display=swap">
<style>
  :root {
    --page-bg: #e9eaee;
    --card-white: #ffffff;
    --gold-dark: #a8741a;
    --gold-mid: #d9a63a;
    --gold-light: #fbf289;
    --ink: #111111;
    --wash-light: #f6efe0;
    --wash-tan: #eadcc0;
  }
  * { box-sizing: border-box; margin: 0; padding: 0; }
  html, body {
    width: 1030px;
    height: 1200px;
    overflow: hidden;
    background: var(--page-bg);
  }
  .header-card {
    position: absolute;
    left: 45px;
    top: 385px;
    width: 940px;
    height: 430px;
    padding: 12px;
    background: linear-gradient(135deg, var(--gold-dark), var(--gold-mid) 30%, var(--gold-light) 50%, var(--gold-mid) 70%, var(--gold-dark));
  }
  .card-face {
    position: relative;
    width: 100%;
    height: 100%;
    background: var(--card-white);
    overflow: hidden;
  }
  .rider-artwork {
    position: absolute;
    left: 30px;
    top: 12px;
    width: 330px;
    height: 180px;
    background: radial-gradient(ellipse at 40% 55%, var(--wash-tan) 0%, var(--wash-light) 55%, rgba(255,255,255,0) 80%);
  }
  .speed-lines {
    position: absolute;
    left: 300px;
    top: 40px;
    width: 500px;
    height: 130px;
    background: linear-gradient(90deg, rgba(246,239,224,0.9), rgba(255,255,255,0));
  }
  .brand-name {
    position: absolute;
    left: 0;
    right: 0;
    top: 92px;
    text-align: center;
    font-family: "Marcellus", serif;
    font-size: 40px;
    letter-spacing: 1px;
    color: var(--ink);
  }
  .title-band {
    position: absolute;
    left: 0;
    right: 0;
    top: 198px;
    height: 92px;
    background: linear-gradient(90deg, var(--gold-dark), var(--gold-mid) 25%, var(--gold-light) 50%, var(--gold-mid) 75%, var(--gold-dark));
    display: flex;
    align-items: center;
    justify-content: center;
  }
  .product-title {
    font-family: "Oswald", sans-serif;
    font-weight: 600;
    font-size: 58px;
    letter-spacing: 1px;
    color: var(--ink);
    text-transform: uppercase;
  }
  .material-line {
    position: absolute;
    left: 0;
    right: 0;
    top: 302px;
    text-align: center;
    font-family: "Open Sans", sans-serif;
    font-weight: 700;
    font-size: 32px;
    color: var(--ink);
  }
</style>
</head>
<body>
  <div class="header-card">
    <div class="card-face">
      <div class="rider-artwork" role="img" aria-label="Faint illustration of a show jumper rider on a horse"></div>
      <div class="speed-lines" role="img" aria-label="Faint sweeping motion streaks"></div>
      <div class="brand-name">TIDEWATER EQUESTRIAN</div>
      <div class="title-band">
        <h1 class="product-title">Equestrian Number Holder</h1>
      </div>
      <p class="material-line">Genuine Leather</p>
    </div>
  </div>
</body>
</html>
```